" Através de um site/aplicativo, conectaremos os turistas que desejam viajar com seu grupo de amigos, famílias, ou empresariais a uma concessionária de aluguel de veículos recreativos (motorhomes) parceiro. Esse parceiro buscará o turista em um local escolhido pelo grupo, e realizará o check-in ali mesmo, e os levará para realizarem o turismo no destino escolhido. O check-out se dará no mesmo local de embarque, sendo flexível aos clientes a montagem da sua Rota Turística. Nosso projeto visa gerar um aproveitamento melhor dos veículos recreativos ociosos, facilitando a conexão desse cliente com uma concessionária, e motoristas já qualificados por outros turistas. Também realizaremos a captação de Estações de Apoio, que são propriedades rurais, utilizadas em regime de economia compartilhada, e utilizada para abrigar as Hospedarias Móveis. Também alimentaremos um blog/rede social com as aventuras vividas por nossos usuários em suas viagens. "

```html
<!DOCTYPE html>
<html lang="pt-BR">
<head>
<meta charset="utf-8">
<title>Rotavia — Cartão de visita</title>
<link href="https://fonts.googleapis.com/css2?family=Arimo:ital,wght@0,400;0,700;1,700&display=swap" rel="stylesheet">
<style>
  :root {
    --backdrop: #ececec;
    --card: #ffffff;
    --orange: #d9782c;
    --logo-orange: #f0a21e;
    --navy: #114e7c;
    --pale-blue: #cfe0ef;
    --ink: #123a5c;
  }
  html, body {
    margin: 0;
    width: 1200px;
    height: 1200px;
    overflow: hidden;
    background: var(--backdrop);
    font-family: "Arimo", Arial, sans-serif;
  }
  .card {
    position: absolute;
    left: 180px;
    width: 840px;
    height: 460px;
    background: var(--card);
    overflow: hidden;
    box-shadow: 0 6px 18px rgba(0,0,0,0.12);
  }
  .card-front { top: 90px; }
  .card-back { top: 640px; }
  .card svg.shapes { position: absolute; inset: 0; }
  .pattern-field {
    position: absolute;
    left: 0; top: 18px;
    width: 840px; height: 230px;
    background: linear-gradient(to bottom, rgba(207,224,239,0.75), rgba(207,224,239,0));
  }
  .brand {
    position: absolute;
    display: flex;
    align-items: center;
    gap: 14px;
    font-weight: 700;
    letter-spacing: 0.5px;
  }
  .brand-dot {
    width: 44px; height: 44px;
    border-radius: 50%;
  }
  .card-front .brand {
    left: 0; right: 0; top: 196px;
    justify-content: center;
    font-size: 56px;
    color: var(--logo-orange);
  }
  .card-front .brand-dot { background: var(--logo-orange); }
  .card-back .brand {
    left: 600px; top: 150px;
    font-size: 38px;
    color: #ffffff;
  }
  .card-back .brand-dot { width: 34px; height: 34px; background: #ffffff; }
  .back-pattern {
    position: absolute;
    left: 20px; top: 250px;
    width: 480px; height: 210px;
    background: linear-gradient(to top, rgba(207,224,239,0.7), rgba(207,224,239,0));
  }
  .holder-name {
    position: absolute;
    left: 66px; top: 52px;
    margin: 0;
    font-size: 31px;
    font-weight: 700;
    color: var(--orange);
  }
  .contact-list {
    position: absolute;
    left: 66px; top: 132px;
    margin: 0; padding: 0;
    list-style: none;
  }
  .contact-list li {
    display: flex;
    align-items: center;
    gap: 12px;
    height: 38px;
    font-size: 21px;
    color: var(--ink);
  }
  .contact-list li.phone { font-weight: 700; }
  .contact-icon {
    width: 22px; height: 22px;
    flex: none;
  }
  .contact-icon.plain { border-radius: 50%; background: var(--orange); }
  .website {
    position: absolute;
    left: 250px; top: 368px;
    font-size: 30px;
    font-weight: 700;
    font-style: italic;
    color: #ffffff;
    letter-spacing: 0.5px;
  }
</style>
</head>
<body>

<section class="card card-front">
  <div class="pattern-field" role="img" aria-label="Padrão suave de triângulos azul-claros"></div>
  <svg class="shapes" width="840" height="460" viewBox="0 0 840 460">
    <polygon points="70,0 770,0 752,18 88,18" fill="var(--orange)"/>
    <polygon points="88,442 752,442 770,460 70,460" fill="var(--orange)"/>
  </svg>
  <div class="brand"><span class="brand-dot"></span>Rotavia</div>
</section>

<section class="card card-back">
  <div class="back-pattern" role="img" aria-label="Padrão suave de triângulos azul-claros"></div>
  <svg class="shapes" width="840" height="460" viewBox="0 0 840 460">
    <polygon points="0,30 18,50 18,460 0,460" fill="var(--orange)"/>
    <polygon points="532,0 546,0 454,460 440,460" fill="var(--pale-blue)"/>
    <polygon points="556,0 840,0 840,460 464,460" fill="var(--navy)"/>
    <polygon points="212,354 840,354 840,425 196,425" fill="var(--orange)"/>
  </svg>

  <h1 class="holder-name">Marcelo Andrade</h1>
  <ul class="contact-list">
    <li class="phone">
      <svg class="contact-icon" viewBox="0 0 24 24"><path fill="var(--orange)" d="M6.6 10.8a15 15 0 0 0 6.6 6.6l2.2-2.2a1 1 0 0 1 1-.25 11.4 11.4 0 0 0 3.6.57 1 1 0 0 1 1 1V20a1 1 0 0 1-1 1A17 17 0 0 1 3 4a1 1 0 0 1 1-1h3.5a1 1 0 0 1 1 1c0 1.25.2 2.45.57 3.57a1 1 0 0 1-.25 1z"/></svg>
      (12) 9.5550-1234
    </li>
    <li>
      <svg class="contact-icon" viewBox="0 0 24 24"><rect x="2" y="5" width="20" height="14" rx="1.5" fill="var(--orange)"/><path d="M3 6l9 7 9-7" fill="none" stroke="#fff" stroke-width="1.8"/></svg>
      contato@rotavia.com.br
    </li>
    <li><span class="contact-icon plain"></span>/ rotavia</li>
    <li><span class="contact-icon plain"></span>/ rotavia</li>
  </ul>

  <div class="brand"><span class="brand-dot"></span>Rotavia</div>
  <div class="website">www.rotavia.com.br</div>
</section>

</body>
</html>
```